Clean business card with logo provided

I want a card that will stand out among the masses. I need the color and image to show professionalism and yet have a family appeal showing that I only deal with win/win scenarios. The back of the card will be used to take notes about the individual so I can use that in my database entry. I like modern design but need professionalism in it also. It needs to fit my "clean, safe, and affordable housing" motto. I need to be able to write on the file and update the card details for my employees.

Target Market(s)

Investors looking to make investment income through real estate

Industry/Entity Type

Real Estate

Contact Information for Business Card

Troy Vandemark
blank address, city, st, zip code
480-555-0147
troyvandemark@quillrentals.example
www.quillrentals.example

Font styles to use
Sans Serif

Requirements
Must have
• I would like the back of the card to have lines for info. example
• Met/Visited: Date:
• Interets:
Nice to have
• I want the cards color to match the logo background color. Font with details to be san serif and black. I want the card rectangular with square corners. Standard business card size. I would like to see cards designed with both images to see which i prefer more.

```html
<!DOCTYPE html>
<html lang="en">
<head>
<meta charset="utf-8">
<title>Quill Rentals LLC — Business Card</title>
<link rel="stylesheet" href="https://fonts.googleapis.com/css2?family=Open+Sans:wght@400;600;700&display=swap">
<style>
  :root {
    --teal: #1cb3cc;
    --ink: #111111;
    --card-black: #000000;
    --paper: #ffffff;
    --stage: #3a3a3a;
    --rule-grey: #555555;
  }
  * { margin: 0; padding: 0; box-sizing: border-box; }
  html, body {
    width: 1200px; height: 900px; overflow: hidden;
    background: var(--stage);
    font-family: "Open Sans", Arial, sans-serif;
  }
  .stage {
    position: relative; width: 1200px; height: 900px;
  }
  .card {
    position: absolute; left: 250px;
    width: 700px; height: 400px;
    border-radius: 18px; overflow: hidden;
  }
  .card--notes { top: 40px; background: var(--paper); }
  .card--contact { top: 460px; background: var(--card-black); }

  .card svg.bands { position: absolute; inset: 0; }

  /* brand lockup */
  .brand { position: absolute; display: flex; flex-direction: column; }
  .brand__name {
    display: flex; align-items: center; gap: 10px;
    font-weight: 700; font-size: 34px; letter-spacing: 3px;
    color: var(--teal); line-height: 1;
  }
  .brand__mark {
    width: 16px; height: 16px; background: var(--teal); border-radius: 50%;
  }
  .brand__tagline {
    margin-top: 8px; font-size: 12px; font-weight: 600; color: var(--teal);
    letter-spacing: 0.2px;
  }
  .card--notes .brand { left: 300px; top: 70px; }
  .card--contact .brand { left: 60px; top: 70px; }

  /* notes side */
  .notes { position: absolute; left: 60px; top: 200px; width: 560px; }
  .notes__heading {
    color: var(--teal); font-weight: 600; font-size: 19px; margin-bottom: 14px;
  }
  .notes__field {
    display: flex; align-items: flex-end; gap: 4px;
    font-size: 16px; color: var(--ink); height: 40px;
  }
  .notes__line { flex: 1; border-bottom: 1.5px dashed #333; margin-bottom: 5px; }

  /* contact side */
  .rule { position: absolute; height: 1px; background: #d0d0d0; }
  .rule--top { left: 250px; right: 30px; top: 70px; }
  .rule--name { left: 60px; width: 330px; top: 284px; }
  .address {
    position: absolute; right: 40px; top: 190px;
    text-align: right; color: var(--paper); font-size: 16px; line-height: 1.3;
  }
  .person {
    position: absolute; left: 60px; top: 240px;
    font-size: 26px; font-weight: 700; letter-spacing: 0.5px;
    color: var(--paper);
  }
  .person__surname { color: var(--teal); }
  .contacts { position: absolute; left: 60px; top: 296px; list-style: none; }
  .contacts li {
    display: flex; align-items: center; gap: 12px;
    color: var(--paper); font-size: 16px; line-height: 22px;
  }
  .contacts svg { width: 14px; height: 14px; flex: none; }
</style>
</head>
<body>
<div class="stage">

  <section class="card card--notes" aria-label="Card back: notes">
    <svg class="bands" viewBox="0 0 700 400" aria-hidden="true">
      <polygon points="0,372 380,372 440,346 700,346 700,400 0,400" fill="var(--paper)"/>
      <polygon points="0,374 420,374 440,390 0,390" fill="var(--teal)"/>
      <polygon points="0,374 400,374 470,360 470,374" fill="var(--teal)"/>
      <rect x="0" y="374" width="440" height="26" fill="var(--teal)"/>
    </svg>
    <div class="brand">
      <div class="brand__name"><span class="brand__mark"></span>QUILL RENTALS LLC</div>
      <div class="brand__tagline">Providing clean, safe, and affordable housing</div>
    </div>
    <div class="notes">
      <p class="notes__heading">Met/Visited:</p>
      <div class="notes__field"><span>Name:</span><span class="notes__line"></span></div>
      <div class="notes__field"><span>Date:</span><span class="notes__line"></span></div>
      <div class="notes__field"><span>Interets:</span><span class="notes__line"></span></div>
    </div>
  </section>

  <section class="card card--contact" aria-label="Card front: contact details">
    <svg class="bands" viewBox="0 0 700 400" aria-hidden="true">
      <polygon points="510,255 700,225 700,282 510,282" fill="var(--teal)"/>
      <polygon points="0,385 510,385 510,282 700,282 700,400 0,400" fill="var(--card-black)"/>
      <polygon points="0,384 480,384 510,372 510,400 0,400" fill="var(--paper)"/>
    </svg>
    <div class="brand">
      <div class="brand__name"><span class="brand__mark"></span>QUILL RENTALS LLC</div>
      <div class="brand__tagline">Providing clean, safe, and affordable housing</div>
    </div>
    <div class="rule rule--top"></div>
    <address class="address" style="font-style:normal">
      2740 Alder Street<br>Brookhaven, OH 44100
    </address>
    <h1 class="person">TROY <span class="person__surname">VANDEMARK</span></h1>
    <div class="rule rule--name"></div>
    <ul class="contacts">
      <li>
        <svg viewBox="0 0 24 24" aria-hidden="true"><path fill="var(--teal)" d="M6.6 10.8a15 15 0 0 0 6.6 6.6l2.2-2.2a1 1 0 0 1 1-.25 11.4 11.4 0 0 0 3.6.6 1 1 0 0 1 1 1V20a1 1 0 0 1-1 1A17 17 0 0 1 3 4a1 1 0 0 1 1-1h3.5a1 1 0 0 1 1 1c0 1.25.2 2.45.6 3.6a1 1 0 0 1-.25 1z"/></svg>
        480-555-0147
      </li>
      <li>
        <svg viewBox="0 0 24 24" aria-hidden="true"><rect x="2" y="5" width="20" height="14" rx="2" fill="none" stroke="var(--teal)" stroke-width="2"/><path d="M3 6l9 7 9-7" fill="none" stroke="var(--teal)" stroke-width="2"/></svg>
        troyvandemark@quillrentals.example
      </li>
      <li>
        <svg viewBox="0 0 24 24" aria-hidden="true"><circle cx="12" cy="12" r="9.5" fill="none" stroke="var(--teal)" stroke-width="2"/><ellipse cx="12" cy="12" rx="4" ry="9.5" fill="none" stroke="var(--teal)" stroke-width="2"/><path d="M2.5 12h19" stroke="var(--teal)" stroke-width="2"/></svg>
        www.quillrentals.example
      </li>
    </ul>
  </section>

</div>
</body>
</html>
```